Make it cool to work near where you are...

Calling all creatives - create the ultimate cool card for people who want to cut their commute.

Here at FarlowBench we've got what can best be described as an Quillet card for desks - and we want to brighten up the wallets of our most loyal users.

So, pitch us your ideas and you might see your design on cards being flashed across the country - and we've thrown in a bit of cash too.

Do see our brief card guidelines - with a couple of past examples thrown in.

```html
<!DOCTYPE html>
<html lang="en">
<head>
<meta charset="utf-8">
<title>FarlowBench membership card</title>
<link rel="stylesheet" href="https://fonts.googleapis.com/css2?family=Lato:wght@400;700&display=swap">
<style>
  :root {
    --canvas-bg: #f2f2f2;
    --card-black: #050305;
    --band-dark: #231f20;
    --art-black: #070408;
    --art-plum: #3a2340;
    --art-lilac: #8e6b93;
    --number-panel: rgba(236, 228, 238, 0.92);
    --number-ink: #1c1a1d;
    --brand-pink: #ec1c7b;
    --text-white: #ffffff;
  }
  * { box-sizing: border-box; margin: 0; padding: 0; }
  html, body {
    width: 1200px;
    height: 1000px;
    overflow: hidden;
    background: var(--canvas-bg);
  }
  .canvas {
    position: relative;
    width: 1200px;
    height: 1000px;
  }
  .card {
    position: absolute;
    width: 600px;
    height: 379px;
    border-radius: 8px;
    overflow: hidden;
    background: var(--card-black);
    font-family: "Lato", sans-serif;
  }
  .card--front { left: 115px; top: 63px; }
  .card--back  { left: 512px; top: 536px; }

  .card__art {
    position: absolute;
    left: 0; top: 0;
    width: 600px;
    height: 303px;
    background: linear-gradient(160deg,
      var(--art-black) 0%,
      var(--art-plum) 30%,
      var(--art-lilac) 45%,
      var(--art-plum) 60%,
      var(--art-black) 85%);
  }
  .card__band {
    position: absolute;
    left: 0; bottom: 0;
    width: 600px;
    height: 76px;
    background: var(--band-dark);
  }
  .card__brand {
    position: absolute;
    left: 46px;
    top: 42px;
    font-weight: 700;
    font-size: 34px;
    line-height: 40px;
    letter-spacing: -0.5px;
    color: var(--brand-pink);
  }
  .card__number {
    position: absolute;
    left: 61px;
    top: 214px;
    width: 280px;
    height: 50px;
    border-radius: 5px;
    background: var(--number-panel);
    color: var(--number-ink);
    font-size: 27px;
    letter-spacing: 1px;
    line-height: 50px;
    text-align: center;
  }
  .card__url {
    position: absolute;
    left: 84px;
    top: 303px;
    width: 400px;
    height: 76px;
    line-height: 76px;
    text-align: center;
    color: var(--text-white);
    font-size: 22px;
    letter-spacing: 0.3px;
  }
  .card__badge {
    position: absolute;
    right: 24px;
    top: 303px;
    height: 76px;
    line-height: 76px;
    color: var(--text-white);
    font-weight: 700;
    font-size: 18px;
  }
</style>
</head>
<body>
<main class="canvas">
  <article class="card card--front">
    <div class="card__art" role="img" aria-label="Abstract flowing lilac and purple light waves on black"></div>
    <div class="card__band"></div>
    <p class="card__brand">FarlowBench</p>
    <p class="card__number">0019821849297</p>
    <p class="card__url">www.deskvale.com/card</p>
    <p class="card__badge">FarlowBench</p>
  </article>

  <article class="card card--back">
    <div class="card__art" role="img" aria-label="Abstract flowing lilac and purple light waves on black"></div>
    <div class="card__band"></div>
    <p class="card__number">0019821849297</p>
    <p class="card__url">www.deskvale.com/card</p>
    <p class="card__badge">FarlowBench</p>
  </article>
</main>
</body>
</html>
```